" A empresa opera inteiramente o segmento de tecnologia e pesquisa, focando no desenvolvimento de soluções únicas e disruptivas, com portifólio próprio de sistemas. "

```html
<!DOCTYPE html>
<html lang="pt-BR">
<head>
<meta charset="UTF-8">
<title>Novara — Papel timbrado</title>
<link rel="stylesheet" href="https://fonts.googleapis.com/css2?family=Montserrat:wght@400;500;700&display=swap">
<style>
  :root {
    --backdrop: #8b4cf2;
    --paper: #ffffff;
    --brand: #8b4cf2;
    --ink: #2f2f35;
    --muted: #8a8a94;
    --footer-band: #38383c;
    --footer-text: #d6d6dc;
  }
  * { margin: 0; padding: 0; box-sizing: border-box; }
  html, body {
    width: 1200px;
    height: 1200px;
    overflow: hidden;
    background: var(--backdrop);
    font-family: "Montserrat", sans-serif;
  }
  .canvas {
    position: relative;
    width: 1200px;
    height: 1200px;
  }
  .letterhead {
    position: absolute;
    left: 300px;
    top: 160px;
    width: 600px;
    height: 880px;
    background: var(--paper);
    display: flex;
    flex-direction: column;
  }
  .letterhead-header {
    display: flex;
    justify-content: space-between;
    align-items: center;
    padding: 52px 48px 0 48px;
  }
  .brand {
    display: flex;
    align-items: center;
    gap: 10px;
  }
  .brand-mark {
    width: 26px;
    height: 26px;
    background: var(--brand);
    border-radius: 3px;
  }
  .brand-name {
    font-weight: 700;
    font-size: 26px;
    letter-spacing: 1px;
    color: var(--ink);
    line-height: 1;
  }
  .brand-tagline {
    font-size: 6px;
    color: var(--muted);
    line-height: 1.3;
    width: 70px;
    margin-left: 2px;
  }
  .site {
    display: flex;
    align-items: center;
    gap: 6px;
    font-size: 10px;
    color: var(--ink);
  }
  .dot {
    width: 10px;
    height: 10px;
    border-radius: 50%;
    background: var(--brand);
    display: inline-block;
  }
  .letterhead-body { flex: 1; }
  .letterhead-footer {
    height: 48px;
    background: var(--footer-band);
    display: flex;
    justify-content: center;
    align-items: center;
    gap: 34px;
    font-size: 9px;
    color: var(--footer-text);
  }
  .contact-item {
    display: flex;
    align-items: center;
    gap: 6px;
  }
  .contact-item .dot { width: 9px; height: 9px; }
</style>
</head>
<body>
  <main class="canvas">
    <article class="letterhead">
      <header class="letterhead-header">
        <div class="brand">
          <span class="brand-mark"></span>
          <span class="brand-name">NOVARA</span>
          <span class="brand-tagline">Smart Systems and Applied Research</span>
        </div>
        <div class="site"><span class="dot"></span>novara.com</div>
      </header>
      <section class="letterhead-body"></section>
      <footer class="letterhead-footer">
        <span class="contact-item"><span class="dot"></span>21 90000-4412</span>
        <span class="contact-item"><span class="dot"></span>contato@novara.com</span>
        <span class="contact-item"><span class="dot"></span>@novara</span>
      </footer>
    </article>
  </main>
</body>
</html>
```